Lantern Harbor of Alabama

We are a disaster relief nonprofit organization that provides relief to families children and pets when a disaster strikes multifamily. We need a easy and powerful piece that tells what we do and draws folks into finding out more. So a piece that could be used at tradeshows or speaking engagements
Updates

Be sure to include our social and other contact info. Added Monday, October 16, 2017

Target Market(s)

Potential Donors & Volunteers

Industry/Entity Type

Non-Profit

Font styles to use
Serif

Colors

Designer to choose colors to be used in the design.

Requirements
Must have
• Our logo and trigger photos I am going to rely on your expertise to create something compelling that is simple and powerful
Nice to have
• Moving pull on the heart strings

```html
<!DOCTYPE html>
<html lang="en">
<head>
<meta charset="utf-8">
<title>Lantern Harbor of Alabama – Postcard</title>
<link href="https://fonts.googleapis.com/css2?family=Marcellus&family=Open+Sans:wght@400;600;700&display=swap" rel="stylesheet">
<style>
  :root{
    --blue:#2f65b8;
    --blue-deep:#234f99;
    --gold:#fbb731;
    --gold-text:#fcc13a;
    --white:#ffffff;
    --page:#8d8d8d;
    --rule:#9a9a9a;
  }
  *{box-sizing:border-box;margin:0;padding:0}
  html,body{width:1200px;height:1200px;overflow:hidden;background:var(--page)}
  body{position:relative;font-family:"Open Sans",sans-serif;color:var(--white)}
  .card{position:absolute;width:749px;height:543px;overflow:hidden;box-shadow:0 3px 10px rgba(0,0,0,.35)}
  .card svg.card-art{position:absolute;inset:0}
  .card-front{left:24px;top:34px}
  .card-back{left:421px;top:621px;background:var(--white)}

  /* front */
  .brand{position:absolute;left:0;width:352px;text-align:center;font-family:"Marcellus",serif;color:var(--white)}
  .brand-name{top:28px;font-size:42px;line-height:44px}
  .brand-sub{top:118px;font-size:13px;letter-spacing:.5px;padding-left:40px}
  .headline{position:absolute;left:0;top:143px;width:408px;text-align:center;font-family:"Marcellus",serif;color:var(--gold-text);font-size:40px;line-height:46px;letter-spacing:.5px}
  .intro{position:absolute;left:20px;top:286px;width:326px;font-size:13px;line-height:17.5px;text-align:justify}
  .call-bar{position:absolute;left:0;top:446px;width:352px;height:40px;background:var(--gold);color:var(--blue-deep);font-family:"Marcellus",serif;font-size:24px;line-height:40px;padding-left:18px}
  .web{position:absolute;left:20px;top:497px;font-size:15px;display:flex;align-items:center;gap:8px}
  .web svg{width:14px;height:14px}

  /* back */
  .kit{position:absolute;left:22px;top:18px;width:432px}
  .kit-title{font-family:"Marcellus",serif;color:var(--gold-text);font-size:25px;line-height:30px;letter-spacing:.5px}
  .kit ul{list-style:none}
  .kit li{color:var(--gold-text);font-weight:700;font-size:12px;line-height:15px;padding-left:12px;position:relative}
  .kit li::before{content:"•";position:absolute;left:0;font-size:10px}
  .kit p{font-size:9.4px;line-height:12.2px;margin:3px 0 6px}
  .kit ul+ul{margin-top:6px}
  .photo-strip{position:absolute;left:0;top:347px;height:100px;width:466px}
  .photo-strip div{position:absolute;top:0;height:100px}
  .mission{position:absolute;left:22px;top:456px;width:448px;font-family:"Marcellus",serif;color:var(--gold-text);font-size:13px;line-height:16px}
  .contact-row{position:absolute;left:22px;top:514px;display:flex;gap:24px;font-size:9.6px;align-items:center}
  .contact-row span{display:flex;align-items:center;gap:8px}
  .contact-row svg{width:11px;height:11px}
  .back-brand{position:absolute;left:528px;top:46px;width:120px;text-align:center;font-family:"Marcellus",serif;color:var(--gold)}
  .back-brand .name{font-size:20px;line-height:20px}
  .back-brand .sub{font-size:6px;margin-top:3px}
  .stamp-box{position:absolute;left:665px;top:37px;width:48px;height:56px;border:1px solid #888}
  .address-line{position:absolute;left:524px;width:185px;height:2px;background:var(--rule)}
  .partners{position:absolute;left:530px;top:513px;display:flex;gap:10px;align-items:center}
  .partners i{display:block;height:10px;background:#b8c3d6;border-radius:2px}
</style>
</head>
<body>

<section class="card card-front">
  <svg class="card-art" width="749" height="543" viewBox="0 0 749 543">
    <defs>
      <linearGradient id="mainPhotoTone" x1="0" y1="0" x2="1" y2="1">
        <stop offset="0" stop-color="#6e5a3f"/>
        <stop offset=".5" stop-color="#d9cbb0"/>
        <stop offset="1" stop-color="#f1f1f1"/>
      </linearGradient>
      <linearGradient id="portraitTone" x1="0" y1="0" x2="1" y2="1">
        <stop offset="0" stop-color="#d8a78c"/>
        <stop offset="1" stop-color="#f3d2c4"/>
      </linearGradient>
    </defs>
    <rect width="749" height="543" fill="var(--blue)"/>
    <path d="M428,0 Q318,270 438,543" fill="none" stroke="var(--gold)" stroke-width="14"/>
    <path d="M442,0 Q332,270 452,543 L749,543 L749,0 Z" fill="var(--white)"/>
    <path d="M450,0 Q340,270 460,543 L749,543 L749,0 Z" fill="url(#mainPhotoTone)" role="img" aria-label="Photo of a smiling boy holding a teddy bear beside a relief kit box"/>
    <circle cx="430" cy="446" r="72" fill="var(--white)"/>
    <circle cx="430" cy="446" r="66" fill="url(#portraitTone)" role="img" aria-label="Portrait of the co-founders, a mother and her son"/>
  </svg>

  <div class="brand brand-name">Lantern<br>Harbor</div>
  <div class="brand brand-sub">of Alabama</div>
  <h1 class="headline">GIVING HOPE<br>WHEN DISASTER<br>STRIKES</h1>
  <p class="intro">Lantern Harbor of Alabama was Co-Founded by Dana Merriweather and her son Miles Merriweather to offer support to Residents that have been displaced from Apartment Homes due to fire or other disasters. Often times, displaced residents are placed in vacant apartments homes or even find themselves on the floor of the clubhouse until a plan is devised for next steps.</p>
  <div class="call-bar">CALL NOW : (205) 555-0147</div>
  <div class="web">
    <svg viewBox="0 0 14 14"><circle cx="7" cy="7" r="6" fill="none" stroke="#fff" stroke-width="1.4"/><path d="M1 7h12M7 1c-3 3-3 9 0 12M7 1c3 3 3 9 0 12" fill="none" stroke="#fff" stroke-width="1"/></svg>
    www.lanternharborofalabama.org
  </div>
</section>

<section class="card card-back">
  <svg class="card-art" width="749" height="543" viewBox="0 0 749 543">
    <path d="M524,0 Q432,300 532,543" fill="none" stroke="var(--gold)" stroke-width="10"/>
    <path d="M512,0 Q420,300 520,543 L0,543 L0,0 Z" fill="var(--blue)"/>
  </svg>

  <div class="kit">
    <h2 class="kit-title">DISASTER RELIEF KIT SUPPLY LIST</h2>
    <ul><li>Twin Air Mattress (8.00 at Brightmart)</li></ul>
    <p>On almost all occasions, property management will place a resident into a vacant apartment. Our disaster relief kits give them everything that victims of disaster need to take refuge for the first few nights. Most often our kits are all that these families have.</p>
    <ul>
      <li>Standard Pillows (2.37 at Brightmart)</li>
      <li>Air Pumps (13.00 Brightmart)</li>
      <li>Blankets/Throws (2.88 at Brightmart)</li>
    </ul>
    <p>Small rolled fleece throws. We also take handmade items/must be new</p>
    <ul>
      <li>Towels/Washcloths/Flat Sheets</li>
      <li>Flip Flops- Solid Colors-All sizes (Brightmart $1)</li>
    </ul>
    <p>Most often victims of disaster are not wearing shoes due to the rushed escape, etc. We provide them with flip flops on scene</p>
    <ul><li>Penny Depot Items All $1</li></ul>
    <p>Brush/Comb Combo, Toothbrush/Paste Travel Combo, Wipes, Deodorant, Hand Sanitizer, Soap, Shampoo, Conditioner<br>We prefer travel sized to ensure that it fits into our boxes and does not leak.</p>
    <ul><li>Cases of Bottled Water</li></ul>
  </div>

  <div class="photo-strip">
    <div style="left:0;width:144px;background:linear-gradient(135deg,#5a3a2c,#c9a36a)" role="img" aria-label="Photo of children receiving stuffed animals"></div>
    <div style="left:148px;width:178px;background:linear-gradient(135deg,#8d9aa5,#4b4f4a)" role="img" aria-label="Photo of rescuers guiding a boat through flood water"></div>
    <div style="left:330px;width:136px;background:linear-gradient(135deg,#3a2418,#e0762a)" role="img" aria-label="Photo of an apartment building on fire"></div>
  </div>

  <p class="mission">Lantern Harbor of Alabama is a Birmingham, Alabama based 501c3 nonprofit organization that provides disaster relief to Residents displaced from Apartment Homes across the state of Alabama.</p>
  <div class="contact-row">
    <span><svg viewBox="0 0 11 11"><circle cx="5.5" cy="5.5" r="5" fill="#fff"/></svg>social.example/lanternharbor</span>
    <span><svg viewBox="0 0 14 14"><circle cx="7" cy="7" r="6" fill="none" stroke="#fff" stroke-width="1.4"/><path d="M1 7h12M7 1c-3 3-3 9 0 12M7 1c3 3 3 9 0 12" fill="none" stroke="#fff" stroke-width="1"/></svg>lanternharborofalabama.org</span>
  </div>

  <div class="back-brand"><div class="name">Lantern<br>Harbor</div><div class="sub">of Alabama</div></div>
  <div class="stamp-box"></div>
  <div class="address-line" style="top:255px"></div>
  <div class="address-line" style="top:284px"></div>
  <div class="address-line" style="top:313px"></div>
  <div class="partners">
    <i style="width:26px"></i><i style="width:30px"></i><i style="width:26px"></i><i style="width:26px"></i><i style="width:26px"></i><i style="width:30px"></i>
  </div>
</section>

</body>
</html>
```